Design few pages for professional development app

I need a website design for a prototype project. The goal of the project is to prototype a few basic screens for a professional development application.

The final design should be clean, modern, and appeal to a professional millenial clientele.The designs have been wireframed (see attached), and we'd like these wireframes converted to design files.

Here is the list of goals and tasks that correspond to the design: https://sheets.plorvane.com/grid/d/7kQWm48p3XZvrt2bYH5LcNaeJoTsUDfi82GhKxMp/edit?view=shared

Number of Pages Required

5+ page

Font styles to use
Serif
Sans Serif

Colors

Designer to choose colors to be used in the design.

Requirements
Nice to have
• Uses Google Material Design, Bootstrap, or another framework

```html
<!DOCTYPE html>
<html lang="en">
<head>
<meta charset="utf-8">
<title>ClimbPath – Take Control of your Career</title>
<link href="https://fonts.googleapis.com/css2?family=Poppins:wght@300;400;500;600;700&family=Open+Sans:wght@400;600&display=swap" rel="stylesheet">
<style>
:root{
  --brand:#2a6783;
  --brand-dark:#214f68;
  --btn:#2a7fae;
  --ink:#1b1b1b;
  --text:#3d3d3d;
  --navy:#2b2f3c;
  --panel-line:#d6dde2;
  --white:#ffffff;
  --footer:#2d303b;
}
*{box-sizing:border-box;margin:0;padding:0}
html,body{width:1200px;height:3753px;overflow:hidden}
body{position:relative;background:var(--white);font-family:"Poppins",sans-serif;color:var(--text)}
.abs{position:absolute}
/* header */
.site-header{left:0;top:0;width:1200px;height:79px;background:var(--white);border-bottom:1px solid #e4e4e4}
.brand-name{left:162px;top:22px;font-weight:700;font-size:31px;color:var(--ink)}
.menu-icon{left:950px;top:32px}
.search-icon{left:1018px;top:28px}
/* hero */
.hero{left:0;top:79px;width:1200px;height:613px;background:linear-gradient(120deg,#6f7f88 0%,#4d6473 40%,#2f4f66 70%,#3a5870 100%)}
.hero-title{left:0;width:1200px;top:250px;text-align:center;font-weight:600;font-size:44px;color:var(--white)}
.hero-text{left:220px;width:760px;top:313px;text-align:center;font-size:22px;line-height:35px;color:var(--white)}
.btn-primary{background:var(--btn);color:var(--white);font-weight:600;display:flex;align-items:center;justify-content:center}
.hero-btn{left:494px;top:440px;width:217px;height:60px;font-size:20px}
/* testimonials */
.avatar{border-radius:50%;background:radial-gradient(circle at 50% 40%,#b9a99a,#5a4c44)}
.quote{font-size:17.5px;line-height:26px;color:var(--text)}
.quote b{display:block;color:var(--brand);font-weight:600}
/* sign up */
.signup{left:0;top:861px;width:1200px;height:654px;background:linear-gradient(100deg,#c9d7de 0%,#dde7ec 45%,#c6d5dd 100%)}
.section-title{left:0;width:1200px;text-align:center;font-weight:600;font-size:34px;color:var(--brand)}
.signup-form{left:329px;top:1019px;width:540px;height:413px;background:var(--navy)}
.field{left:368px;width:461px;height:49px;background:var(--white);border:1px solid #cfcfcf;font-size:15px;color:#444;padding:17px 0 0 19px}
.checkbox{left:372px;top:1302px;width:18px;height:18px;background:var(--white)}
.check-label{left:402px;top:1302px;font-size:13px;color:#3a3f4d}
.signup-btn{left:371px;top:1341px;width:220px;height:48px;font-size:19px}
.learn-btn{left:608px;top:1341px;width:220px;height:48px;border:2px solid var(--btn);color:var(--white);font-weight:600;font-size:17px;display:flex;align-items:center;justify-content:center}
/* goals */
.goals-sub{left:0;width:1200px;top:1612px;text-align:center;font-size:19px;color:var(--brand)}
.goal{left:389px;width:409px;height:70px;border:2px solid #dcdcdc;background:var(--white);box-shadow:0 1px 3px rgba(0,0,0,.08)}
.goal-check{position:absolute;left:20px;top:19px}
.goal-icon{position:absolute;left:93px;top:21px}
.goal-label{position:absolute;left:135px;top:20px;font-weight:600;font-size:20px;color:#333}
.list-btn{left:479px;top:2037px;width:223px;height:43px;border:2px solid #8a8a8a;font-size:13.5px;color:#333;display:flex;align-items:center;justify-content:center}
/* tasks */
.tasks{left:0;top:2150px;width:1200px;height:640px;background:var(--brand)}
.tasks-title{left:0;width:1200px;top:2208px;text-align:center;font-weight:300;font-size:32px;color:var(--white)}
.task-card{width:283px;height:193px;border:1px solid #7fa3b6}
.task-head{position:absolute;left:0;top:0;width:100%;height:48px;background:var(--brand-dark);color:var(--white);font-weight:600;font-size:15px;padding:15px 0 0 26px}
.task-desc{position:absolute;left:20px;top:70px;width:250px;font-family:"Open Sans",sans-serif;font-size:13px;line-height:17px;color:#e3edf2;text-transform:uppercase}
.task-btn{position:absolute;left:16px;top:136px;width:248px;height:43px;background:var(--white);color:var(--brand);font-weight:600;font-size:15px;display:flex;align-items:center;justify-content:center;gap:6px}
/* article */
.author-name{left:246px;top:2928px;font-size:17px;color:#222}
.author-role{left:246px;top:2961px;font-size:13px;color:#222}
.article-text{left:160px;top:3036px;width:295px;font-family:"Open Sans",sans-serif;font-size:13.6px;line-height:28.5px;color:#222}
.video{left:504px;top:3020px;width:509px;height:309px;background:linear-gradient(135deg,#4a5560,#2a323a 60%,#3c454e)}
.frame-line{background:#222}
.play{left:722px;top:3131px}
.notes{left:157px;top:3387px;width:862px;height:224px;border:1px solid #d3d3d3;box-shadow:0 1px 4px rgba(0,0,0,.1);padding:38px 50px}
.notes h3{font-family:"Open Sans",sans-serif;font-weight:600;font-size:17px;color:var(--brand);margin-bottom:18px}
.notes p{font-family:"Open Sans",sans-serif;font-size:17px;line-height:29px;color:var(--btn)}
/* footer */
.site-footer{left:0;top:3674px;width:1200px;height:79px;background:var(--footer);color:#e0e0e0;font-family:"Open Sans",sans-serif;font-size:15px;text-align:center;padding-top:30px}
</style>
</head>
<body>

<header class="abs site-header">
  <div class="abs brand-name">ClimbPath</div>
  <svg class="abs menu-icon" width="36" height="22" viewBox="0 0 36 22" aria-hidden="true"><rect y="2" width="36" height="3" fill="#666"/><rect y="9" width="36" height="3" fill="#666"/><rect y="16" width="36" height="3" fill="#666"/></svg>
  <svg class="abs search-icon" width="24" height="24" viewBox="0 0 24 24" aria-hidden="true"><circle cx="10" cy="10" r="7" fill="none" stroke="#888" stroke-width="3"/><line x1="15" y1="15" x2="22" y2="22" stroke="#888" stroke-width="3.5"/></svg>
</header>

<section class="abs hero" role="img" aria-label="Photo of two colleagues reviewing work on a tablet at a desk"></section>
<h1 class="abs hero-title">Take Control of your Career</h1>
<p class="abs hero-text">Complete short, actionable tasks guaranteed to get you further in your career, faster than ever. Ready to get started? Take the short quiz below and get your personalized path today.</p>
<a class="abs btn-primary hero-btn">GET STARTED</a>

<div class="abs avatar" style="left:181px;top:726px;width:88px;height:88px" role="img" aria-label="Portrait of Nora Ellis"></div>
<p class="abs quote" style="left:284px;top:732px;width:290px">I love how quickly I can do the tasks, and see progress.<b>Nora Ellis</b></p>
<div class="abs avatar" style="left:623px;top:726px;width:88px;height:88px" role="img" aria-label="Portrait of Owen Hartley"></div>
<p class="abs quote" style="left:726px;top:732px;width:290px">The best investment I've made in myself in ages.<b>Owen Hartley</b></p>

<section class="abs signup" role="img" aria-label="Faded photo of a desk with laptop, charts and papers"></section>
<h2 class="abs section-title" style="top:932px">Sign Up To See &amp; Save Your Goals</h2>
<form class="abs signup-form"></form>
<div class="abs field" style="top:1059px">Name</div>
<div class="abs field" style="top:1117px">*Email</div>
<div class="abs field" style="top:1175px">* Password</div>
<div class="abs field" style="top:1233px">* Re-type password</div>
<div class="abs checkbox"></div>
<div class="abs check-label">I agree to the terms and privacy policy</div>
<a class="abs btn-primary signup-btn">SIGN UP</a>
<a class="abs learn-btn">LEARN MORE</a>

<h2 class="abs section-title" style="top:1556px">What Are Your Main Goals?</h2>
<p class="abs goals-sub">Tell us what you would like to achieve with ClimbPath</p>

<div class="abs goal" style="top:1679px">
  <svg class="goal-check" width="30" height="30" viewBox="0 0 30 30"><circle cx="15" cy="15" r="14" fill="var(--btn)"/><path d="M8 15.5l5 5 9-10" fill="none" stroke="#fff" stroke-width="3"/></svg>
  <svg class="goal-icon" width="30" height="26" viewBox="0 0 30 26"><circle cx="8" cy="7" r="4" fill="#888"/><circle cx="22" cy="7" r="4" fill="#888"/><circle cx="15" cy="10" r="5" fill="#777"/><path d="M1 20c0-5 4-7 7-7s5 1 6 3M29 20c0-5-4-7-7-7s-5 1-6 3" fill="#888"/><path d="M6 26c0-6 4-9 9-9s9 3 9 9z" fill="#777"/></svg>
  <span class="goal-label">Build my network</span>
</div>
<div class="abs goal" style="top:1761px">
  <svg class="goal-check" width="30" height="30" viewBox="0 0 30 30"><circle cx="15" cy="15" r="14" fill="var(--btn)"/><path d="M8 15.5l5 5 9-10" fill="none" stroke="#fff" stroke-width="3"/></svg>
  <svg class="goal-icon" width="30" height="26" viewBox="0 0 30 26"><circle cx="8" cy="7" r="4" fill="#888"/><circle cx="22" cy="7" r="4" fill="#888"/><circle cx="15" cy="10" r="5" fill="#777"/><path d="M6 26c0-6 4-9 9-9s9 3 9 9z" fill="#777"/></svg>
  <span class="goal-label">Personal branding</span>
</div>
<div class="abs goal" style="top:1846px">
  <svg class="goal-check" width="30" height="30" viewBox="0 0 30 30"><circle cx="15" cy="15" r="14" fill="var(--btn)"/><path d="M8 15.5l5 5 9-10" fill="none" stroke="#fff" stroke-width="3"/></svg>
  <svg class="goal-icon" width="30" height="26" viewBox="0 0 30 26"><circle cx="8" cy="7" r="4" fill="#888"/><circle cx="22" cy="7" r="4" fill="#888"/><circle cx="15" cy="10" r="5" fill="#777"/><path d="M6 26c0-6 4-9 9-9s9 3 9 9z" fill="#777"/></svg>
  <span class="goal-label">Get a promotion</span>
</div>
<div class="abs goal" style="top:1932px">
  <svg class="goal-check" width="30" height="30" viewBox="0 0 30 30"><circle cx="15" cy="15" r="14" fill="var(--btn)"/><path d="M8 15.5l5 5 9-10" fill="none" stroke="#fff" stroke-width="3"/></svg>
  <svg class="goal-icon" width="30" height="26" viewBox="0 0 30 26"><circle cx="8" cy="7" r="4" fill="#888"/><circle cx="22" cy="7" r="4" fill="#888"/><circle cx="15" cy="10" r="5" fill="#777"/><path d="M6 26c0-6 4-9 9-9s9 3 9 9z" fill="#777"/></svg>
  <span class="goal-label">Be a bettter leader</span>
</div>
<a class="abs list-btn">See My Personalized List</a>

<section class="abs tasks"></section>
<h2 class="abs tasks-title">Nora, here's your list of suggested tasks</h2>

<div class="abs task-card" style="left:160px;top:2298px"><div class="task-head">PERSONAL BRANDING</div><p class="task-desc">Write your personal brand statement</p><a class="task-btn"><svg width="16" height="16" viewBox="0 0 16 16"><rect x="1" y="3" width="11" height="11" fill="none" stroke="currentColor" stroke-width="2"/><path d="M4 8l3 3 8-9" fill="none" stroke="currentColor" stroke-width="2"/></svg>COMPLETED</a></div>
<div class="abs task-card" style="left:459px;top:2299px"><div class="task-head">GET A PROMOTION</div><p class="task-desc">Have a career conversation with your manager</p><a class="task-btn"><svg width="20" height="20" viewBox="0 0 20 20"><circle cx="10" cy="10" r="10" fill="currentColor"/><path d="M8 5.5v9l7-4.5z" fill="#fff"/></svg>START TASK</a></div>
<div class="abs task-card" style="left:759px;top:2298px"><div class="task-head">GET A PROMOTION</div><p class="task-desc">Ask 4 peers for candid feedback</p><a class="task-btn"><svg width="20" height="20" viewBox="0 0 20 20"><circle cx="10" cy="10" r="10" fill="currentColor"/><path d="M8 5.5v9l7-4.5z" fill="#fff"/></svg>START TASK</a></div>
<div class="abs task-card" style="left:160px;top:2512px"><div class="task-head">PERSONAL BRANDING</div><p class="task-desc">Write your personal brand statement</p><a class="task-btn"><svg width="20" height="20" viewBox="0 0 20 20"><circle cx="10" cy="10" r="10" fill="currentColor"/><path d="M8 5.5v9l7-4.5z" fill="#fff"/></svg>START</a></div>
<div class="abs task-card" style="left:459px;top:2513px"><div class="task-head">GET A PROMOTION</div><p class="task-desc">Have a career conversation with your manager</p><a class="task-btn"><svg width="20" height="20" viewBox="0 0 20 20"><circle cx="10" cy="10" r="10" fill="currentColor"/><path d="M8 5.5v9l7-4.5z" fill="#fff"/></svg>START</a></div>
<div class="abs task-card" style="left:759px;top:2512px"><div class="task-head">GET A PROMOTION</div><p class="task-desc">Ask 4 peers for candid feedback</p><a class="task-btn"><svg width="20" height="20" viewBox="0 0 20 20"><circle cx="10" cy="10" r="10" fill="currentColor"/><path d="M8 5.5v9l7-4.5z" fill="#fff"/></svg>START</a></div>

<h2 class="abs section-title" style="top:2846px">Learn about Career Conversations</h2>
<div class="abs avatar" style="left:162px;top:2922px;width:70px;height:70px" role="img" aria-label="Portrait of author Samir Cole"></div>
<div class="abs author-name">By Samir Cole</div>
<div class="abs author-role">Senior Marketing Leader, Northvane Co</div>
<p class="abs article-text">Lorem ipsum dolor sit amet, consectetur adipiscing elit. Vivamus rhoncus vulputate sollicitudin. Ut commodo gravida orci vel mattis. Mauris vitae elit dui. Donec enim enim, euismod a felis ac, aliquam varius leo. Etiam pretium pharetra leo, vitae scelerisque est egestas convallis. Interdum et malesuada fames ac ante ipsum primis in faucibus. Vivamus vel egestas ex, et molestie enim. Pellentesque nec mollis</p>

<div class="abs frame-line" style="left:494px;top:3008px;width:177px;height:2px"></div>
<div class="abs frame-line" style="left:494px;top:3008px;width:2px;height:60px"></div>
<div class="abs frame-line" style="left:1019px;top:3230px;width:2px;height:111px"></div>
<div class="abs frame-line" style="left:844px;top:3339px;width:177px;height:2px"></div>
<div class="abs video" role="img" aria-label="Video still of hands reviewing financial charts on a desk"></div>
<svg class="abs play" width="76" height="76" viewBox="0 0 76 76" aria-label="Play video"><circle cx="38" cy="38" r="38" fill="#fff"/><path d="M31 26v24l19-12z" fill="#111"/></svg>

<aside class="abs notes">
  <h3>Lorem ipsum dolor sit amet, consectetur adipiscing elit.</h3>
  <p>+ Vivamus rhoncus vulputate sollicitudin.</p>
  <p>+ Ut commodo gravida orci vel mattis.</p>
  <p>+ Mauris vitae elit dui. Donec enim enim, euismod a felis ac, aliquam varius leo.</p>
</aside>

<footer class="abs site-footer">© 2019 Company Name &nbsp;All right reserved</footer>

</body>
</html>
```